Create Illustration about method for buy a ticket

Create an image that makes you understand the 3 steps for buying tickets for your event

1) Enter your email
2) Make the payment
3) Complete the procedure by entering your data (name and phone number)

(And down explain)
*if you lose your ticket or not finish procedure, you can retrieve it via the email entered

Use the graphic line of the [login to view URL]

**** COMPANY
The company sell tickets for for event and concert.
site: [login to view URL]

**** ASSETS OF COMPANY
Color: RED ( #ff3d3e ) BLUE ( #2b3643 )
Font: raleway ( [login to view URL] )

```html
<!DOCTYPE html>
<html lang="en">
<head>
<meta charset="utf-8">
<title>3 Steps for buying tickets for your event</title>
<link rel="stylesheet" href="https://fonts.googleapis.com/css2?family=Raleway:ital,wght@0,500;0,600;1,500&display=swap">
<style>
  :root {
    --brand-red: #ff3d3e;
    --brand-blue: #2b3643;
    --panel: #ffffff;
    --disc: #e6e7e9;
    --ink: #2b3643;
  }
  * { margin: 0; padding: 0; box-sizing: border-box; }
  html, body { width: 1200px; height: 936px; overflow: hidden; }
  body {
    background: var(--brand-blue);
    font-family: "Raleway", sans-serif;
    color: var(--ink);
    position: relative;
  }
  .panel {
    position: absolute;
    left: 80px; top: 64px;
    width: 1040px; height: 715px;
    background: var(--panel);
  }
  .title {
    position: absolute;
    left: 0; right: 0; top: 129px;
    text-align: center;
    font-weight: 600;
    font-size: 29px;
    letter-spacing: 0.1px;
  }
  .title-rule {
    position: absolute;
    left: 576px; top: 181px;
    width: 47px; height: 3px;
    background: var(--brand-red);
  }
  .step-visual {
    position: absolute;
    width: 200px; height: 260px;
  }
  .step-visual .disc { fill: var(--disc); }
  .step-visual .phone { fill: none; stroke: var(--brand-red); stroke-width: 3; }
  .icon-dark { fill: none; stroke: var(--ink); stroke-width: 2.6; stroke-linejoin: round; stroke-linecap: round; }
  .icon-red { fill: none; stroke: var(--brand-red); stroke-width: 2.6; stroke-linecap: round; stroke-linejoin: round; }
  .step-label {
    position: absolute;
    width: 320px;
    text-align: center;
    font-weight: 500;
    font-size: 21px;
    line-height: 26px;
  }
  .step-label small {
    display: block;
    font-size: 15px;
    line-height: 20px;
  }
  .flow-arrow { position: absolute; left: 0; top: 0; }
  .flow-arrow path { fill: none; stroke: var(--brand-red); stroke-width: 2.5; stroke-dasharray: 8 6; stroke-linecap: round; }
  .flow-arrow .head { stroke-dasharray: none; }
  .note {
    position: absolute;
    left: 216px; top: 628px;
    width: 768px; height: 55px;
    border-radius: 28px;
    background: var(--brand-blue);
    color: #ffffff;
    font-style: italic;
    font-weight: 500;
    font-size: 16.5px;
    display: flex; align-items: center; justify-content: center;
  }
  .note .mark { color: var(--brand-red); font-size: 22px; margin-right: 8px; font-style: normal; }
</style>
</head>
<body>
  <div class="panel"></div>

  <h1 class="title">3 Steps for buying tickets for your event</h1>
  <div class="title-rule"></div>

  <!-- Step 1: email -->
  <svg class="step-visual" style="left:173px; top:253px" viewBox="0 0 200 260" aria-hidden="true">
    <circle class="disc" cx="100" cy="130" r="96"/>
    <rect class="phone" x="47" y="7" width="107" height="191" rx="10"/>
    <rect class="phone" x="56" y="42" width="90" height="122"/>
    <rect class="phone" x="88" y="19" width="24" height="8" rx="4"/>
    <circle class="phone" cx="100" cy="182" r="8"/>
    <rect class="icon-dark" x="72" y="86" width="56" height="38" rx="3"/>
    <path class="icon-red" d="M72 89 L100 108 L128 89"/>
  </svg>

  <!-- Step 2: payment -->
  <svg class="step-visual" style="left:499px; top:253px" viewBox="0 0 200 260" aria-hidden="true">
    <circle class="disc" cx="100" cy="130" r="96"/>
    <rect class="phone" x="47" y="7" width="107" height="191" rx="10"/>
    <rect class="phone" x="56" y="42" width="90" height="122"/>
    <rect class="phone" x="88" y="19" width="24" height="8" rx="4"/>
    <circle class="phone" cx="100" cy="182" r="8"/>
    <rect class="icon-dark" x="74" y="84" width="58" height="36" rx="4"/>
    <rect class="icon-dark" x="68" y="92" width="58" height="36" rx="4" style="fill:#fff"/>
    <line class="icon-dark" x1="68" y1="101" x2="126" y2="101"/>
    <line class="icon-red" x1="75" y1="112" x2="96" y2="112"/>
    <line class="icon-red" x1="75" y1="118" x2="88" y2="118"/>
    <circle class="icon-red" cx="111" cy="116" r="3"/>
    <circle class="icon-red" cx="117" cy="116" r="3"/>
  </svg>

  <!-- Step 3: details -->
  <svg class="step-visual" style="left:828px; top:253px" viewBox="0 0 200 260" aria-hidden="true">
    <circle class="disc" cx="100" cy="130" r="96"/>
    <rect class="phone" x="45" y="7" width="109" height="191" rx="10"/>
    <rect class="phone" x="55" y="42" width="90" height="122"/>
    <rect class="phone" x="88" y="19" width="24" height="8" rx="4"/>
    <circle class="phone" cx="100" cy="182" r="8"/>
    <path class="icon-dark" d="M86 100 V78 H108 L116 86 V100"/>
    <line class="icon-red" x1="92" y1="86" x2="104" y2="86"/>
    <line class="icon-red" x1="92" y1="93" x2="110" y2="93"/>
    <path class="icon-dark" d="M72 128 V92 H84 L88 97 V100"/>
    <path class="icon-dark" style="fill:#fff" d="M72 128 L80 100 H130 L122 128 Z"/>
    <path class="icon-red" d="M92 114 L99 120 L110 106"/>
  </svg>

  <svg class="flow-arrow" width="1200" height="936" aria-hidden="true">
    <path d="M384 363 Q420 395 480 390"/>
    <path class="head" d="M471 381 L483 390 L471 398"/>
    <path d="M711 400 Q750 368 810 373"/>
    <path class="head" d="M800 365 L813 373 L801 382"/>
  </svg>

  <p class="step-label" style="left:113px; top:500px">Enter your email</p>
  <p class="step-label" style="left:439px; top:500px">Make the payment</p>
  <p class="step-label" style="left:768px; top:500px">Complete the procedure<br>by entering your data<small>(name and phone number)</small></p>

  <p class="note"><span class="mark">*</span>if you lose your ticket or not finish procedure, you can retrieve it via the email entered</p>
</body>
</html>
```